Feminine colorfull packaging for coconut skin care brand

We need a design that can be used on different types of packaging for beauty products likes creams, oils, etc.
The products that we will launch will be made with one key ingredient of coconut oil + other added ingredients depending on the type of product. The entire marketing will therefore be based on COCONUTS, palmtrees, sand, beach, bronzing on the beach, holiday feeling, nature, femininity, etc. = A Lifestyle brand with a tropical vibe.
Packaging can be a pot for creams, flaskes for lotions, smaller bottles for oils, etc. Mostly the standard packaging used for beauty products.
We would like to use the color pink ( this can be bright or pastel or any tone of pink) to address the feminine side of our product and a tone of blue-green ( pastel, bright or any tone of this color) to accentuate the use of coconut.
Third would be the color white (this can be added through an accent somewhere on the packaging or this can be the brand name that is written in white)
Lastely we would like the packaging to be light, fresh and playfull. Please feel free to use different colors or shapes ( we do not yet have a logo. This can then be designed followed on the packaging)
The design will be printed on plastic packaging. We are open to very creative designs. We are looking for packaging that catches the eye by its design and/or colors, that is different than others, that distinguishes the product because of its packaging design.
Target Market(s)
Women between 20 - 35 years
Industry/Entity Type
Beauty
Colors
Designer to choose colors to be used in the design.
Look and feel

```html
<!DOCTYPE html>
<html lang="en">
<head>
<meta charset="utf-8">
<title>Palmiva – Coconut Body Lotion Label</title>
<link rel="stylesheet" href="https://fonts.googleapis.com/css2?family=Caveat+Brush&display=swap">
<style>
  :root {
    --page-bg: #f1f1f1;
    --label-pink: #f4a7b1;
    --label-teal: #7ecdd0;
    --label-white: #ffffff;
    --art-white-soft: rgba(255, 255, 255, 0.55);
    --art-white-faint: rgba(255, 255, 255, 0.18);
  }
  * { margin: 0; padding: 0; box-sizing: border-box; }
  html, body {
    width: 1200px;
    height: 1200px;
    overflow: hidden;
    background: var(--page-bg);
  }
  .canvas {
    position: relative;
    width: 1200px;
    height: 1200px;
    display: flex;
    align-items: center;
    justify-content: center;
  }
  .label {
    position: relative;
    width: 520px;
    height: 1100px;
    border-radius: 64px;
    overflow: hidden;
    background: var(--label-pink);
  }
  .label-bands {
    position: absolute;
    inset: 0;
    width: 100%;
    height: 100%;
  }
  .band { fill: var(--label-teal); }
  .art-shells {
    position: absolute;
    left: 40px;
    top: 10px;
    width: 460px;
    height: 200px;
    border-radius: 40px;
    background: linear-gradient(160deg, var(--art-white-faint), rgba(126, 205, 208, 0.25));
  }
  .art-palms {
    position: absolute;
    left: 20px;
    top: 470px;
    width: 480px;
    height: 630px;
    border-radius: 40px 40px 0 0;
    background: linear-gradient(180deg, var(--art-white-soft) 0%, var(--art-white-faint) 100%);
  }
  .brand-name {
    position: absolute;
    left: 0;
    right: 0;
    top: 290px;
    text-align: center;
    font-family: "Caveat Brush", cursive;
    font-size: 150px;
    line-height: 1;
    color: var(--label-white);
  }
</style>
</head>
<body>
  <main class="canvas">
    <section class="label">
      <svg class="label-bands" viewBox="0 0 520 1100" aria-hidden="true">
        <polygon class="band" points="520,50 520,190 0,680 0,500"/>
        <polygon class="band" points="520,230 520,260 0,760 0,720"/>
        <polygon class="band" points="520,560 520,720 0,1060 0,900"/>
        <polygon class="band" points="520,470 520,490 60,830 40,820"/>
      </svg>
      <div class="art-shells" role="img" aria-label="Line illustration of seashells and a starfish with scattered teal dots"></div>
      <div class="art-palms" role="img" aria-label="White silhouette illustration of three tall palm trees"></div>
      <h1 class="brand-name">Palmiva</h1>
    </section>
  </main>
</body>
</html>
```